Bright Tooth Dentistry Business Card

We need business cards for our dental office.
We are looking for a clean, elegant design

We provide dental services to children.
Our card needs to be appealing to referring dentists, parents and our team

Target Market(s)

referring dentists, parents and our team

Industry/Entity Type

Dental Clinic

Contact Information for Business Card

4816 Juniper Lane, Suite 100
Cedar Hollow, PA 15237

412-837-2961 Voice
412-837-2962 fax
info@brighttoothdentalpa.com email
www.brighttoothdentalpa.com web

Font styles to use
Sans Serif

Requirements
Must have
• White background - clean, crisp, elegant, simple
• rounded corners
• different color palate - once we come up with design, we will replace the blue with orange, green,
Nice to have
• Follow our logo typeface and colors
• then we can replace color

```html
<!DOCTYPE html>
<html lang="en">
<head>
<meta charset="utf-8">
<title>Bright Tooth Dentistry – Business Card</title>
<link rel="stylesheet" href="https://fonts.googleapis.com/css2?family=Open+Sans:wght@400&family=Quicksand:wght@400;700&display=swap">
<style>
  :root {
    --brand-blue: #02aceb;
    --ink: #4a4a4a;
    --muted: #6b6b6b;
    --paper: #ffffff;
    --backdrop: #ebebeb;
  }
  * { margin: 0; padding: 0; box-sizing: border-box; }
  html, body { width: 1200px; height: 800px; overflow: hidden; background: var(--backdrop); }
  .stage { position: relative; width: 1200px; height: 800px; }

  .card {
    position: absolute;
    left: 316px;
    width: 570px;
    height: 330px;
    border-radius: 18px;
    overflow: hidden;
  }
  .card--front { top: 50px; background: var(--brand-blue); }
  .card--back { top: 418px; background: var(--paper); }

  .front-brand {
    position: absolute;
    left: 0; right: 0; top: 186px;
    text-align: center;
    font-family: "Quicksand", sans-serif;
    font-weight: 700;
    font-size: 40px;
    line-height: 48px;
    color: var(--paper);
    letter-spacing: -0.5px;
  }

  .back-brand {
    position: absolute;
    right: 16px; top: 84px;
    font-family: "Quicksand", sans-serif;
    font-weight: 700;
    font-size: 26px;
    line-height: 32px;
    color: var(--brand-blue);
    letter-spacing: -0.3px;
  }

  .person-name {
    position: absolute;
    left: 17px; top: 166px;
    font-family: "Quicksand", sans-serif;
    font-weight: 700;
    font-size: 19px;
    color: var(--brand-blue);
  }
  .person-role {
    position: absolute;
    left: 17px; top: 193px;
    font-family: "Quicksand", sans-serif;
    font-weight: 400;
    font-size: 16px;
    color: var(--muted);
  }
  .role-rule {
    position: absolute;
    left: 75px; right: 16px; top: 205px;
    height: 1px;
    background: var(--brand-blue);
  }

  .contact-list {
    position: absolute;
    left: 17px; top: 229px;
    list-style: none;
    font-family: "Open Sans", sans-serif;
    font-size: 13px;
    color: var(--ink);
  }
  .contact-list li {
    display: flex; align-items: center;
    height: 21.5px;
  }
  .contact-list svg { width: 11px; height: 11px; margin-right: 7px; fill: var(--brand-blue); }
  .web-domain { color: var(--brand-blue); }

  .address {
    position: absolute;
    right: 16px; top: 279px;
    text-align: right;
    font-family: "Open Sans", sans-serif;
    font-style: normal;
    font-size: 13px;
    line-height: 16px;
    color: var(--ink);
  }
</style>
</head>
<body>
<main class="stage">
  <section class="card card--front" aria-label="Card front">
    <div class="front-brand">Bright Tooth Dentistry</div>
  </section>

  <section class="card card--back" aria-label="Card back">
    <div class="back-brand">Bright Tooth Dentistry</div>

    <div class="person-name">Lena Marchetti</div>
    <div class="person-role">Doctor</div>
    <div class="role-rule"></div>

    <ul class="contact-list">
      <li>
        <svg viewBox="0 0 24 24" aria-hidden="true"><path d="M6.6 10.8a15 15 0 0 0 6.6 6.6l2.2-2.2a1 1 0 0 1 1-.25 11.4 11.4 0 0 0 3.6.57 1 1 0 0 1 1 1V20a1 1 0 0 1-1 1A17 17 0 0 1 3 4a1 1 0 0 1 1-1h3.5a1 1 0 0 1 1 1c0 1.25.2 2.45.57 3.57a1 1 0 0 1-.25 1z"/></svg>
        412-837-2961
      </li>
      <li>
        <svg viewBox="0 0 24 24" aria-hidden="true"><path d="M6 2h12v5H6zM3 8h18a1 1 0 0 1 1 1v8h-4v5H6v-5H2V9a1 1 0 0 1 1-1zm5 8v4h8v-4z"/></svg>
        412-837-2962
      </li>
      <li>
        <svg viewBox="0 0 24 24" aria-hidden="true"><path d="M2 4h20v16H2zm2 3v11h16V7l-8 6z"/></svg>
        info@brighttoothdentalpa.com
      </li>
      <li>
        <svg viewBox="0 0 24 24" aria-hidden="true"><path d="M12 2a10 10 0 1 0 0 20 10 10 0 0 0 0-20zm-1 17.9A8 8 0 0 1 4.2 10L9 14.8V16a2 2 0 0 0 2 2zm6.9-2.5A2 2 0 0 0 16 16h-1v-3a1 1 0 0 0-1-1H8v-2h2a1 1 0 0 0 1-1V7h2a2 2 0 0 0 2-2v-.4a8 8 0 0 1 2.9 12.8z"/></svg>
        www.<span class="web-domain">brighttoothdentalpa</span>.com
      </li>
    </ul>

    <address class="address">
      4816 Juniper Lane, Suite 100<br>
      Cedar Hollow, PA 15237
    </address>
  </section>
</main>
</body>
</html>
```